Steady Bloomwell HEMP Cannabis CBD tinctures

We need packaging for our line of CBD product label design based in Oakland Ca Brand is called 'Steady Bloomwell'. Our initial product is tincture to help people with pain with out the High effect of THC. I will be attaching og other company sample. The design should communicate slick look and relay health. Use the logo as way to color

Target Market(s)

CBD

Font styles to use
Serif
Decorative

Requirements
Must have
• Design that will make it stand out from the rest of the product on the shelve and be bright.
Nice to have
• The package must be able to stand out and not be dominated by Black color the green color must be the main color.
Should not have
• Be all black and get lost on the shelves

```html
<!DOCTYPE html>
<html lang="en">
<head>
<meta charset="utf-8">
<title>Steady Bloomwell CBD Tincture Label</title>
<link href="https://fonts.googleapis.com/css2?family=Oswald:wght@600&family=Montserrat:wght@500;600&display=swap" rel="stylesheet">
<style>
  :root {
    --page: #f3f4f3;
    --label: #f7f8f7;
    --green: #2fa84a;
    --green-mid: #5fcf73;
    --green-soft: #a9e8b3;
    --green-pale: #d9f5de;
    --grey-dark: #7a7a7a;
    --grey-text: #5c5c5c;
    --white: #ffffff;
  }
  * { margin: 0; padding: 0; box-sizing: border-box; }
  html, body { width: 1200px; height: 1200px; overflow: hidden; background: var(--page); }
  .label {
    position: absolute; left: 160px; top: 50px;
    width: 880px; height: 1100px;
    background: radial-gradient(ellipse at center, var(--white) 45%, var(--label) 100%);
    border-top: 10px solid var(--green);
    overflow: hidden;
    font-family: "Montserrat", sans-serif;
  }
  .wave {
    position: absolute; top: 0; width: 230px; height: 1000px;
  }
  .wave--left { left: 0; background: linear-gradient(90deg, rgba(169,232,179,0.15), rgba(95,207,115,0.55) 55%, rgba(255,255,255,0)); border-radius: 0 60% 60% 0 / 0 50% 50% 0; }
  .wave--right { right: 0; background: linear-gradient(270deg, rgba(169,232,179,0.15), rgba(95,207,115,0.55) 55%, rgba(255,255,255,0)); border-radius: 60% 0 0 60% / 50% 0 0 50%; }
  .type-tag {
    position: absolute; left: 270px; top: 48px; width: 340px; height: 50px;
  }
  .type-tag span {
    position: absolute; inset: 0; display: flex; align-items: center; justify-content: center;
    color: var(--white); font-size: 36px; font-weight: 500; letter-spacing: 1px;
  }
  .brand-mark {
    position: absolute; left: 380px; top: 190px; width: 120px; height: 120px;
    background: var(--green); border-radius: 18px;
  }
  .brand-name {
    position: absolute; left: 0; right: 0; top: 398px; text-align: center;
    color: var(--green); font-size: 48px; font-weight: 600;
  }
  .product {
    position: absolute; left: 0; right: 0; top: 520px; text-align: center;
    font-family: "Oswald", sans-serif; font-weight: 600; color: var(--green);
    font-size: 236px; line-height: 1; letter-spacing: -4px;
  }
  .rule { position: absolute; left: 255px; width: 370px; height: 4px; background: var(--green); border-radius: 2px; }
  .rule--top { top: 758px; }
  .rule--bottom { top: 824px; }
  .subtitle {
    position: absolute; left: 0; right: 0; top: 768px; text-align: center;
    color: var(--grey-text); font-size: 38px; font-weight: 600; letter-spacing: 1px;
  }
  .strength {
    position: absolute; left: 0; right: 0; top: 838px; text-align: center;
    font-family: "Oswald", sans-serif; font-weight: 600; color: var(--green);
    font-size: 122px; line-height: 1;
  }
  .base-band {
    position: absolute; left: 0; right: 0; bottom: 0; height: 100px;
    background: linear-gradient(180deg, var(--green-soft), var(--green-pale));
  }
  .volume-tab { position: absolute; left: 265px; top: 995px; width: 350px; height: 54px; }
  .volume-tab span {
    position: absolute; inset: 0; display: flex; align-items: center; justify-content: center;
    color: var(--white); font-size: 34px; font-weight: 500;
  }
</style>
</head>
<body>
  <div class="label">
    <div class="wave wave--left" role="img" aria-label="Flowing green ribbon decoration"></div>
    <div class="wave wave--right" role="img" aria-label="Flowing green ribbon decoration"></div>

    <div class="type-tag">
      <svg width="340" height="50" viewBox="0 0 340 50"><polygon points="0,0 340,0 326,50 14,50" fill="#7a7a7a"/></svg>
      <span>TINCTURE</span>
    </div>

    <div class="brand-mark"></div>
    <div class="brand-name">Steady Bloomwell</div>

    <div class="product">CBD</div>
    <div class="rule rule--top"></div>
    <div class="subtitle">HEMP EXTRACT</div>
    <div class="rule rule--bottom"></div>
    <div class="strength">1500MG</div>

    <div class="base-band"></div>
    <div class="volume-tab">
      <svg width="350" height="54" viewBox="0 0 350 54"><polygon points="18,0 332,0 350,54 0,54" fill="#6cc47b"/></svg>
      <span>15ML</span>
    </div>
  </div>
</body>
</html>
```